Kestrel Facility Systems needs a business card design with logo

need a business card and log design for a company called "Kestrel Facility Systems". we improve building energy efficiency and save energy costs through building automation systems for commercial buildings such as hospitals, office buildings, universities, etc. The final design should communicate elements such as "precision", "energy efficiency", "green buildings". back side should list our service offerings

```html
<!DOCTYPE html>
<html lang="en">
<head>
<meta charset="utf-8">
<title>Kestrel Facility Systems — Business Card</title>
<link rel="stylesheet" href="https://fonts.googleapis.com/css2?family=Exo+2:wght@700;800&family=Roboto:wght@400&display=swap">
<style>
  :root {
    --backdrop: #e9e4dc;
    --card-white: #ffffff;
    --card-black: #000000;
    --green-deep: #00a651;
    --green-light: #52bd6e;
    --brand-green: #109a47;
    --accent-green: #7cc242;
    --text-light: #ffffff;
  }
  * { margin: 0; padding: 0; box-sizing: border-box; }
  html, body { width: 900px; height: 1200px; overflow: hidden; }
  body { background: var(--backdrop); position: relative; font-family: "Roboto", Arial, sans-serif; }

  .card {
    position: absolute; left: 88px; width: 734px; height: 430px;
    border-radius: 24px; overflow: hidden;
  }
  .card--front { top: 125px; background: var(--card-white); }
  .card--back { top: 640px; background: var(--card-black); }

  .front-wave { position: absolute; inset: 0; }

  .brand-dot {
    position: absolute; border-radius: 50%; background: var(--green-deep);
  }
  .card--front .brand-dot { left: 136px; top: 25px; width: 136px; height: 136px; }
  .card--back .brand-dot { left: 285px; top: 72px; width: 156px; height: 156px; }

  .brand-name {
    position: absolute; left: 0; width: 100%; text-align: center;
    font-family: "Exo 2", Arial, sans-serif; font-weight: 800;
    letter-spacing: 0.5px; line-height: 1;
  }
  .card--front .brand-name { left: 40px; width: 354px; top: 200px; color: var(--brand-green); font-size: 27px; }
  .card--back .brand-name { top: 240px; color: var(--text-light); font-size: 28px; }

  .brand-sub {
    position: absolute; display: flex; align-items: center; gap: 10px;
    font-family: "Exo 2", Arial, sans-serif; font-weight: 800; line-height: 1;
  }
  .brand-sub::before, .brand-sub::after { content: ""; flex: 1; height: 2px; background: var(--green-deep); }
  .card--front .brand-sub { left: 49px; width: 336px; top: 233px; font-size: 19px; color: var(--brand-green); }
  .card--back .brand-sub { left: 193px; width: 336px; top: 272px; font-size: 19px; color: var(--text-light); }

  .holder { position: absolute; left: 49px; top: 330px; color: var(--text-light); }
  .holder-name { font-family: "Exo 2", Arial, sans-serif; font-weight: 800; font-size: 23px; letter-spacing: 0.8px; line-height: 1; }
  .holder-role { font-family: "Exo 2", Arial, sans-serif; font-weight: 700; font-size: 12.5px; letter-spacing: 0.5px; margin-top: 4px; }

  .divider { position: absolute; left: 270px; top: 293px; width: 2px; height: 112px; background: var(--text-light); }

  .contact-list { position: absolute; left: 296px; top: 290px; list-style: none; color: var(--text-light); font-size: 16.5px; }
  .contact-list li { display: flex; align-items: center; height: 23.3px; }
  .contact-list svg { width: 15px; height: 15px; margin-right: 14px; flex: none; fill: var(--text-light); }

  .services { position: absolute; left: 0; top: 315px; width: 100%; text-align: center; color: var(--text-light); font-size: 15.5px; line-height: 23px; }
  .services .sep { display: inline-block; width: 6px; height: 6px; border-radius: 50%; background: var(--accent-green); margin: 0 9px 2px; }
</style>
</head>
<body>

<section class="card card--front">
  <svg class="front-wave" viewBox="0 0 734 430" preserveAspectRatio="none" aria-hidden="true">
    <defs>
      <linearGradient id="waveFill" x1="0" y1="0" x2="1" y2="0">
        <stop offset="0" stop-color="#52bd6e"/>
        <stop offset="0.5" stop-color="#00a651"/>
        <stop offset="1" stop-color="#00a651"/>
      </linearGradient>
    </defs>
    <path d="M0,255 C200,292 470,240 734,150 L734,430 L0,430 Z" fill="url(#waveFill)"/>
  </svg>

  <div class="brand-dot"></div>
  <div class="brand-name">KESTREL FACILITY</div>
  <div class="brand-sub">SYSTEMS</div>

  <div class="holder">
    <div class="holder-name">OWEN HARTLEY</div>
    <div class="holder-role">MANAGING DIRECTOR</div>
  </div>

  <div class="divider"></div>

  <ul class="contact-list">
    <li><svg viewBox="0 0 24 24"><path d="M6.6 10.8a15 15 0 0 0 6.6 6.6l2.2-2.2c.3-.3.7-.4 1-.2 1.1.4 2.3.6 3.6.6.6 0 1 .4 1 1V20c0 .6-.4 1-1 1A17 17 0 0 1 3 4c0-.6.4-1 1-1h3.5c.6 0 1 .4 1 1 0 1.3.2 2.5.6 3.6.1.3 0 .7-.2 1z"/></svg>02 8004 1172</li>
    <li><svg viewBox="0 0 24 24"><path d="M7 1h10a2 2 0 0 1 2 2v18a2 2 0 0 1-2 2H7a2 2 0 0 1-2-2V3a2 2 0 0 1 2-2zm0 3v13h10V4zm5 15a1.2 1.2 0 1 0 0 2.4 1.2 1.2 0 0 0 0-2.4z"/></svg>0412 556 309</li>
    <li><svg viewBox="0 0 24 24"><path d="M2 5h20v14H2zm2 2v.5l8 5 8-5V7l-8 5z"/></svg>owen@kestrelfacilitysystems.com</li>
    <li><svg viewBox="0 0 24 24"><path d="M12 2a10 10 0 1 0 0 20 10 10 0 0 0 0-20zm6.9 9h-3a15 15 0 0 0-1.3-6 8 8 0 0 1 4.3 6zM12 4c.9 1.2 1.8 3.6 2 7h-4c.2-3.4 1.1-5.8 2-7zM9.4 5a15 15 0 0 0-1.3 6h-3a8 8 0 0 1 4.3-6zm-4.3 8h3a15 15 0 0 0 1.3 6 8 8 0 0 1-4.3-6zM12 20c-.9-1.2-1.8-3.6-2-7h4c-.2 3.4-1.1 5.8-2 7zm2.6-1a15 15 0 0 0 1.3-6h3a8 8 0 0 1-4.3 6z"/></svg>www.kestrelfacilitysystems.com</li>
    <li><svg viewBox="0 0 24 24"><path d="M12 1a8 8 0 0 0-8 8c0 6 8 14 8 14s8-8 8-14a8 8 0 0 0-8-8zm0 11a3 3 0 1 1 0-6 3 3 0 0 1 0 6z"/></svg>#210 118 Harbourview Road, Vancouver Canada</li>
  </ul>
</section>

<section class="card card--back">
  <div class="brand-dot"></div>
  <div class="brand-name">KESTREL FACILITY</div>
  <div class="brand-sub">SYSTEMS</div>

  <p class="services">
    Building automation systems<span class="sep"></span>Building automation systems<span class="sep"></span>Building automation systems<br>
    Building automation systems<span class="sep"></span>Building automation systems
  </p>
</section>

</body>
</html>
```